Marlow Creek Stud website

We would like to create a horse stud/agistment farm website similar to this websites we have attached below:
www.hollistead.com.au
www.quandrell.com.au
www.barrowick.com
www.fenshaw.com.au
The main colour scheme are purple and white to align with the stable's racing colours.
We have also attach the company logo and also images of the farm and create some ideas for the website.
Many thanks for looking into this project!

```html
<!DOCTYPE html>
<html lang="en">
<head>
<meta charset="utf-8">
<title>Marlow Creek Stud</title>
<link href="https://fonts.googleapis.com/css2?family=Gelasio:wght@400&family=Montserrat:wght@500;600&display=swap" rel="stylesheet">
<style>
:root{
  --purple:#3b1642;
  --purple-soft:#5a2a63;
  --ink:#1f1a22;
  --grey-band:#f7f7f7;
  --white:#ffffff;
  --rule:#9a9a9a;
}
*{margin:0;padding:0;box-sizing:border-box}
html,body{width:1200px;height:2711px;overflow:hidden;background:var(--white)}
body{position:relative;font-family:"Gelasio",Georgia,serif;color:var(--ink)}
.abs{position:absolute}
.brand-mark{left:62px;top:62px;font-family:"Gelasio",Georgia,serif;font-size:24px;color:var(--purple);display:flex;align-items:center;gap:10px}
.brand-mark .dot{width:22px;height:22px;border-radius:50%;background:var(--purple)}
.social{display:flex;gap:26px}
.social span{width:16px;height:16px;border-radius:50%;background:var(--purple-soft)}
.header-social{left:1020px;top:44px}
.nav{top:114px;left:0;width:1200px;font-family:"Montserrat",Arial,sans-serif;font-size:13px;font-weight:600;letter-spacing:2.3px;color:var(--ink)}
.nav a{position:absolute;text-decoration:none;color:inherit;white-space:nowrap}
.hero{left:0;top:157px;width:1200px;height:707px;background:linear-gradient(180deg,#3a3630 0%,#6d5f4f 40%,#b9a99b 58%,#c65a7a 78%,#4f7a3a 90%,#3f6a2e 100%)}
.hero-dots{left:545px;top:818px;display:flex;gap:10px}
.hero-dots span{width:12px;height:12px;border-radius:50%;background:var(--white)}
.hero-dots span.active{background:var(--purple)}
.intro-mark{left:0;width:1200px;top:972px;text-align:center}
.intro-mark .dot{display:inline-block;width:80px;height:80px;border-radius:50%;background:var(--purple)}
.intro-title{left:0;width:1200px;top:1096px;text-align:center;font-size:36px;color:var(--purple)}
.intro-sub{left:0;width:1200px;top:1145px;text-align:center;font-family:"Montserrat",Arial,sans-serif;font-weight:500;font-size:17px;letter-spacing:4px;color:#444}
.intro-copy{left:175px;width:850px;top:1196px;text-align:center;font-size:13.5px;line-height:23px}
.btn{display:flex;align-items:center;justify-content:center;background:var(--purple);color:var(--white);border-radius:23px;font-family:"Montserrat",Arial,sans-serif;font-weight:500;font-size:12px;letter-spacing:2.5px;height:45px}
.intro-btn{left:524px;top:1308px;width:164px}
.dotted-rule{left:226px;top:1402px;width:755px;border-top:2px dotted var(--rule)}
.photo{display:block}
.photo-horses{left:222px;top:1424px;width:372px;height:278px;background:linear-gradient(180deg,#4f8fd6 0%,#a8c9ee 55%,#4f8a36 72%,#6aa23e 100%)}
.photo-paddock{left:611px;top:1424px;width:372px;height:278px;background:linear-gradient(180deg,#4d5a70 0%,#a9a39a 45%,#6e5a36 70%,#3e4a22 100%)}
.photo-aerial{left:155px;top:1718px;width:593px;height:335px;background:linear-gradient(180deg,#3d7fd0 0%,#a9c8ea 30%,#5f8a3f 50%,#3f6f2c 80%,#2f5a22 100%)}
.section-title{font-size:36px;color:var(--purple)}
.facilities-title{left:779px;top:1744px}
.facilities-copy{left:779px;top:1810px;width:236px;font-size:13.5px;line-height:23.3px}
.news-band{left:0;top:2123px;width:1200px;height:452px;background:var(--grey-band)}
.news-photo{left:258px;top:2224px;width:240px;height:240px;border-radius:50%;background:linear-gradient(180deg,#2c2a2f 0%,#7d6e70 45%,#b9a6c2 65%,#c65a7a 85%,#e0a23c 100%)}
.news-title{left:564px;top:2227px}
.news-copy{left:564px;top:2283px;width:505px;font-size:13.5px;line-height:23.3px}
.news-btn{left:819px;top:2425px;width:188px}
.footer{left:0;top:2575px;width:1200px;height:136px;background:var(--purple);color:var(--white);font-size:13.5px;line-height:19.5px}
.footer-address{left:233px;top:38px}
.footer-links{left:560px;width:138px;top:38px;text-align:center}
.footer-social{left:884px;top:44px}
.footer-social span{background:var(--white)}
.footer-copy{left:810px;top:88px;font-size:11px}
</style>
</head>
<body>

<header>
  <div class="abs brand-mark"><span class="dot"></span>Marlow Creek Stud</div>
  <div class="abs social header-social" aria-label="Social links"><span></span><span></span><span></span></div>
  <nav class="abs nav">
    <a href="#" style="left:410px">HOME</a>
    <a href="#" style="left:520px">STALLIONS</a>
    <a href="#" style="left:679px">BROOM MARES</a>
    <a href="#" style="left:865px">ABOUT THE FARM</a>
    <a href="#" style="left:1055px">CONTACT</a>
  </nav>
</header>

<section>
  <div class="abs hero" role="img" aria-label="Grey racehorse galloping with jockey in purple and white silks past flower beds at a night race meeting"></div>
  <div class="abs hero-dots"><span class="active"></span><span></span><span></span></div>
</section>

<section>
  <div class="abs intro-mark"><span class="dot"></span></div>
  <h1 class="abs intro-title" style="font-weight:400">MC stallions, distinguished by excellence</h1>
  <p class="abs intro-sub">MARLOW CREEK STUD</p>
  <p class="abs intro-copy">Lorem ipsum dolor sit amet, consectetur adipiscing elit. Quisque condimentum vel orci lacinia blandit. Cras et gravida elit, ut vestibulum libero. Curabitur non justo non sapien semper tincidunt sed a magna. In id porta magna, ac feugiat dui. Nam ultrices risus sit amet ante viverra pulvinar. Nulla at orci ante. Suspendisse eget varius massa.</p>
  <a class="abs btn intro-btn" href="#">LEARN MORE</a>
  <div class="abs dotted-rule"></div>
</section>

<section>
  <div class="abs photo photo-horses" role="img" aria-label="Five young horses standing in a green paddock under blue sky"></div>
  <div class="abs photo photo-paddock" role="img" aria-label="Timber paddock fence and pasture at sunset under cloudy sky"></div>
  <div class="abs photo photo-aerial" role="img" aria-label="Aerial view of the farm stables, laneways and green paddocks with hills behind"></div>
  <h2 class="abs section-title facilities-title" style="font-weight:400">Facilities</h2>
  <p class="abs facilities-copy">Lorem ipsum dolor sit amet, consectetur adipiscing elit. Quisque condimentum vel orci lacinia blandit. Cras et gravida elit, ut vestibulum libero. Curabitur non justo non sapien semper tincidunt sed a magna. In id porta magna, ac feugiat dui. Nam ultrices risus sit amet ante viverra pulvinar. Nulla at orci ante. Suspendisse eget varius massa.</p>
</section>

<section>
  <div class="abs news-band"></div>
  <div class="abs news-photo" role="img" aria-label="Racehorse and jockey in purple silks crossing the finish line"></div>
  <h2 class="abs section-title news-title" style="font-weight:400">News</h2>
  <p class="abs news-copy">Lorem ipsum dolor sit amet, consectetur adipiscing elit. Quisque condimentum vel orci lacinia blandit. Cras et gravida elit, ut vestibulum libero. Curabitur non justo non sapien semper tincidunt sed a magna. In id porta magna, ac feugiat dui. Nam ultrices risus sit amet ante viverra pulvinar. Nulla at orci ante. Suspendisse eget varius massa.</p>
  <a class="abs btn news-btn" href="#">LEARN MORE</a>
</section>

<footer class="abs footer">
  <div class="abs footer-address">Marlow Creek Stud<br>Ashvale,<br>Phone: +61 400 555 018</div>
  <div class="abs footer-links">Stallions<br>Stud<br>News</div>
  <div class="abs social footer-social" aria-label="Social links"><span></span><span></span><span></span></div>
  <div class="abs footer-copy">© 2019 MC Stud All rights reserved</div>
</footer>

</body>
</html>
```